Design some Business Cards for Larkfen Spirits

Design a business card for Larkfen Spirits

We are a small high end Larkfen Spirits Company, we make Vodka, Gin, Rums and other stuff

Create front & back business card using theme colours logo supplied, needs to have the following details:

Name
Tittle

Phone number
Fax number
Mobile number
email
website larkfenspirits.com

Address

300 dpi and resolution of 3000 in the following format:
EPS
JPEG
PDF
PNG
PSD

We will be using http://www.quillpress-example.com.hk/en/finishing.htm for printing of business cards, so any "Goldstamping" or "Embossing" needs to be in there format for the printers

We have over 30 brands which will need logos, so whoever wins this one will be invited back for them first

```html
<!DOCTYPE html>
<html lang="en">
<head>
<meta charset="utf-8">
<title>Larkfen Spirits – Business Card Front</title>
<link rel="stylesheet" href="https://fonts.googleapis.com/css2?family=Cinzel:wght@600&family=Raleway:wght@500&display=swap">
<style>
  :root {
    --page: #ffffff;
    --card-dark: #050505;
    --card-mid: #2a2a2a;
    --brand-red: #c9402b;
    --ink-light: #f4f1ea;
    --gold-pale: #fbf3d6;
    --gold-mid: #e6c98c;
    --gold-deep: #b5823f;
    --bronze: #9a5f2a;
  }
  * { margin: 0; padding: 0; box-sizing: border-box; }
  html, body {
    width: 1200px;
    height: 685px;
    overflow: hidden;
    background: var(--page);
  }
  .card {
    position: relative;
    width: 1200px;
    height: 685px;
    border-radius: 36px;
    overflow: hidden;
    background: radial-gradient(ellipse 45% 50% at 50% 42%, var(--card-mid) 0%, #141414 55%, var(--card-dark) 100%);
  }
  .side-tab {
    position: absolute;
    top: 240px;
    width: 120px;
    height: 205px;
  }
  .side-tab--left { left: 0; }
  .side-tab--right { right: 0; }
  .base-band {
    position: absolute;
    left: 0;
    bottom: 0;
    width: 100%;
    height: 58px;
    background: linear-gradient(90deg, var(--bronze) 0%, var(--gold-deep) 12%, var(--gold-mid) 30%, var(--gold-pale) 50%, var(--gold-mid) 70%, var(--gold-deep) 88%, var(--bronze) 100%);
  }
  .brand-name {
    position: absolute;
    left: 0;
    width: 100%;
    text-align: center;
    font-family: "Cinzel", serif;
    font-weight: 600;
    color: var(--brand-red);
    line-height: 1;
    letter-spacing: 2px;
  }
  .brand-name--first { top: 150px; font-size: 80px; }
  .brand-name--second { top: 318px; font-size: 68px; }
  .brand-mark {
    position: absolute;
    left: 576px;
    top: 250px;
    width: 48px;
    height: 48px;
    border-radius: 50%;
    background: var(--brand-red);
  }
  .tagline {
    position: absolute;
    left: 0;
    top: 402px;
    width: 100%;
    text-align: center;
    font-family: "Raleway", sans-serif;
    font-weight: 500;
    font-size: 14px;
    letter-spacing: 0.5px;
    color: var(--ink-light);
  }
  .flourish {
    position: absolute;
    left: 447px;
    top: 428px;
    width: 300px;
    height: 100px;
    background: radial-gradient(ellipse 50% 50% at 50% 45%, rgba(246,232,189,0.85) 0%, rgba(230,201,140,0.55) 40%, rgba(181,130,63,0.25) 70%, rgba(181,130,63,0) 100%);
  }
</style>
</head>
<body>
  <main class="card">
    <svg class="side-tab side-tab--left" viewBox="0 0 120 205" aria-hidden="true">
      <defs>
        <linearGradient id="tabGoldLeft" x1="0" y1="0" x2="1" y2="0">
          <stop offset="0" stop-color="#c79a55"/>
          <stop offset="0.35" stop-color="#f6e8bd"/>
          <stop offset="1" stop-color="#fdf7e0"/>
        </linearGradient>
      </defs>
      <polygon points="0,0 80,0 118,102 80,205 0,205" fill="url(#tabGoldLeft)"/>
    </svg>

    <svg class="side-tab side-tab--right" viewBox="0 0 120 205" aria-hidden="true">
      <defs>
        <linearGradient id="tabGoldRight" x1="1" y1="0" x2="0" y2="0">
          <stop offset="0" stop-color="#c79a55"/>
          <stop offset="0.35" stop-color="#f6e8bd"/>
          <stop offset="1" stop-color="#fdf7e0"/>
        </linearGradient>
      </defs>
      <polygon points="120,0 40,0 2,102 40,205 120,205" fill="url(#tabGoldRight)"/>
    </svg>

    <div class="brand-name brand-name--first">LARKFEN</div>
    <span class="brand-mark" aria-hidden="true"></span>
    <div class="brand-name brand-name--second">SPIRITS</div>

    <p class="tagline">PREMIUM LIQUOR COMPANY</p>

    <div class="flourish" role="img" aria-label="Gold ornamental scroll flourish beneath the company name"></div>

    <div class="base-band" aria-hidden="true"></div>
  </main>
</body>
</html>
```